Talvoro Card Design Project

Our company,Talvoro, is focusing B to B, and people receiving this card are managers or engineers in the handset maker in the world.
Therefore we hope this to be designed strictly serious one but it needs cool and unique style which could imagine something innovation from the card.

This card will be used for Japanese,Chinese and English.
Please consider 2 byte character usage.

Industry/Entity Type

It Company

```html
<!DOCTYPE html>
<html lang="en">
<head>
<meta charset="utf-8">
<title>Talvoro Business Card</title>
<link rel="stylesheet" href="https://fonts.googleapis.com/css2?family=Questrial&display=swap">
<style>
  :root {
    --stage: #8d8d8d;
    --stage-light: #b4b4b4;
    --card-white: #fbfbfb;
    --card-grey: #e6e6e6;
    --ink-dark: #4a4a4a;
    --ink-mid: #6e6e6e;
    --ink-light: #a9a9a9;
    --band-light: #c9c9c9;
    --band-dark: #6a6a6a;
    --panel-dark: #8a8a8a;
    --back-bg-1: #dcdcdc;
    --back-bg-2: #c4c4c4;
  }
  * { margin: 0; padding: 0; box-sizing: border-box; }
  html, body {
    width: 1200px; height: 1200px; overflow: hidden;
  }
  body {
    background: radial-gradient(circle at 50% 45%, var(--stage-light), var(--stage) 75%);
    font-family: "Questrial", "Century Gothic", sans-serif;
    position: relative;
  }
  .card {
    position: absolute;
    left: 170px;
    width: 860px;
    height: 491px;
    overflow: hidden;
    box-shadow: 0 10px 30px rgba(0,0,0,0.28);
  }
  /* Front */
  .card-front {
    top: 80px;
    background: linear-gradient(135deg, var(--card-white) 0%, var(--card-white) 55%, var(--card-grey) 100%);
  }
  .brand {
    position: absolute;
    left: 80px; top: 330px;
    display: flex; align-items: center; gap: 14px;
  }
  .brand-mark {
    width: 30px; height: 30px;
    background: var(--ink-mid);
  }
  .brand-name {
    font-size: 44px;
    color: var(--ink-mid);
    letter-spacing: 1px;
  }
  .top-band {
    position: absolute;
    left: 480px; top: 150px;
    width: 380px; height: 30px;
    background: var(--band-light);
  }
  .person-name {
    position: absolute;
    left: 350px; top: 96px;
    font-size: 50px;
    color: var(--ink-mid);
  }
  .person-role {
    position: absolute;
    right: 120px; top: 150px;
    font-size: 20px;
    color: var(--ink-light);
  }
  .info-bar {
    position: absolute;
    left: 355px; top: 225px;
    width: 505px; height: 30px;
    display: flex;
  }
  .info-bar .seg-dark { width: 150px; background: var(--band-dark); }
  .info-bar .seg-light { flex: 1; background: var(--band-light); }
  .contact {
    position: absolute;
    left: 355px; top: 290px;
    list-style: none;
    font-size: 22px;
    color: var(--ink-dark);
    line-height: 31px;
  }
  .contact li { display: flex; align-items: center; gap: 8px; }
  .contact svg { width: 20px; height: 20px; fill: var(--ink-dark); flex: none; }
  /* Back */
  .card-back {
    top: 631px;
    background: linear-gradient(90deg, var(--back-bg-1), var(--back-bg-2));
  }
  .back-panel {
    position: absolute;
    right: 0; top: 0;
    width: 250px; height: 100%;
    background: var(--panel-dark);
  }
  .back-name {
    position: absolute;
    left: 60px; top: 170px;
    font-size: 130px;
    color: var(--ink-mid);
    letter-spacing: 2px;
    line-height: 1;
  }
  .back-url {
    position: absolute;
    left: 70px; top: 320px;
    font-size: 30px;
    color: var(--ink-mid);
    letter-spacing: 3px;
  }
</style>
</head>
<body>
  <section class="card card-front">
    <div class="brand">
      <span class="brand-mark"></span>
      <span class="brand-name">TALVORO</span>
    </div>
    <div class="top-band"></div>
    <h1 class="person-name">Business Name</h1>
    <div class="person-role">Position</div>
    <div class="info-bar"><span class="seg-dark"></span><span class="seg-light"></span></div>
    <ul class="contact">
      <li>18 Unit/4 Harbor City, NY</li>
      <li><svg viewBox="0 0 20 20" aria-hidden="true"><path d="M2 7c0-3 3-4 8-4s8 1 8 4v2h-4V7H6v2H2z M5 10h10l2 7H3z"/></svg>0431 582017</li>
      <li><svg viewBox="0 0 20 20" aria-hidden="true"><path d="M2 5h16v11H2z M3 6l7 5 7-5" fill="none" stroke="#4a4a4a" stroke-width="1.6"/></svg>talvoroofficial@email.com</li>
      <li><svg viewBox="0 0 20 20" aria-hidden="true"><circle cx="10" cy="10" r="7" fill="none" stroke="#4a4a4a" stroke-width="2"/><path d="M4 10h12" stroke="#4a4a4a" stroke-width="2"/></svg>www.talvoro.com</li>
    </ul>
  </section>

  <section class="card card-back">
    <div class="back-panel"></div>
    <div class="back-name">TALVORO</div>
    <div class="back-url">www.talvorostudio.com</div>
  </section>
</body>
</html>
```